kel varnto website design

An IT support and IT Security Company - just use dummy text for now for the design. Examples of sites we like the looks and feel of but need it more professional feel are like: www.brovaquent.uk.com , www.plimdore.co.uk, www.quastenvel.com/professional/, www.vio.com, www.mulvex.com,

Best to message me if you have any questions

Target Market(s)

small to medium UK based companies that require IT support services

Industry/Entity Type

It Company

Contact Information for Business Card

use dummy name, telephone and email for now, will provide details later.

Logo Text

kel varnto (and then below the logo it should say "your IT, networks and security partner")

Coding

Coded - Design and coding required

Number of Pages Required

5+ page

Colors

Designer to choose colors to be used in the design.

Requirements
Must have
• must be professional, yet simple and clear that this is a serious IT support and IT security company.
Nice to have
• 1)The website homepage must have professional quality pictures of IT support or London city skyline or any picture that projects friendly business partners, professionalism and ready to serve.
• 2) Home page needs to include tabs for following pages 'Services' , 'About Us' , 'Contact Us' 'Home'
• 3) Website built customised using wordpress is ideal and easy for us to manage.
• more room for boxed options from homepage (with pic or image in background)
Should not have
• no checkout trolleys or payment options.

```html
<!DOCTYPE html>
<html lang="en">
<head>
<meta charset="UTF-8">
<title>kel varnto — IT Support &amp; Security</title>
<link href="https://fonts.googleapis.com/css2?family=Poppins:wght@400;500;600&family=Open+Sans:wght@400;600&display=swap" rel="stylesheet">
<style>
:root{
  --blue:#1b8fd9;
  --blue-dark:#0f7fc7;
  --ink:#111;
  --muted:#555;
  --grey-band:#ebebeb;
  --footer:#000;
  --white:#fff;
  --star:#f5a623;
}
*{margin:0;padding:0;box-sizing:border-box}
html,body{width:1200px;height:2965px;overflow:hidden}
body{position:relative;font-family:"Open Sans",Arial,sans-serif;color:var(--ink);background:var(--white)}
.abs{position:absolute}
h1,h2,h3,h4,.logo,.nav a{font-family:"Poppins",Arial,sans-serif}

/* hero */
.hero{left:0;top:0;width:1200px;height:682px}
.hero-photo{position:absolute;inset:0;background:linear-gradient(110deg,#3c4a4a 0%,#55605c 35%,#6d6a66 55%,#3f4845 80%,#2f3a37 100%)}
.hero-shade{position:absolute;inset:0;background:linear-gradient(90deg,rgba(0,0,0,.35),rgba(0,0,0,.05))}
.logo{color:var(--white);font-size:25px;font-weight:500}
.hero .logo{left:87px;top:54px}
.nav{left:0;top:63px;width:1200px;height:20px}
.nav a{position:absolute;top:0;white-space:nowrap;color:var(--white);font-size:13px;font-weight:500;text-decoration:none}
.nav a.active{color:var(--blue)}
.nav svg{position:absolute;left:1097px;top:3px}
.hero h1{left:87px;top:296px;width:700px;color:var(--white);font-size:44px;font-weight:500;line-height:53px}
.hero-link{left:89px;top:430px;color:var(--blue);font-size:14px;text-decoration:none}
.scroll-btn{left:88px;top:629px;width:104px;height:104px;border-radius:50%;background:var(--blue);box-shadow:0 8px 20px rgba(0,0,0,.25);z-index:2}

/* about */
.about{left:0;top:682px;width:1200px;height:609px;background:#fff}
.skyline{position:absolute;left:0;right:0;bottom:0;height:330px;background:linear-gradient(180deg,rgba(255,255,255,1) 0%,rgba(240,214,200,.8) 30%,#9a7b70 62%,#3f3535 80%,#1e2428 100%)}
.eyebrow{width:1200px;text-align:center;color:var(--blue);font-family:"Poppins",Arial,sans-serif;font-size:12px;font-weight:500;letter-spacing:.5px}
.section-title{width:1200px;text-align:center;font-size:31px;font-weight:500;color:var(--ink)}
.about-text{left:230px;width:740px;text-align:center;font-size:13px;line-height:26px;color:var(--muted)}
.btn{left:540px;top:285px;width:122px;height:35px;background:var(--blue);color:var(--white);font-family:"Poppins",Arial,sans-serif;font-size:11px;font-weight:600;display:flex;align-items:center;justify-content:center}

/* service boxes */
.service{top:1291px;width:600px;height:389px;text-align:center}
.service.support{left:0;background:linear-gradient(135deg,#2a9be0,#1389d5 60%,#0f80cb)}
.service.security{left:600px;background:#fff}
.service svg{position:absolute;left:265px;top:118px}
.service h3{position:absolute;top:198px;width:100%;font-size:18px;font-weight:500}
.service p{position:absolute;top:232px;left:140px;width:320px;font-size:11.5px;line-height:22px}
.support h3,.support p{color:var(--white)}
.security p{color:var(--muted)}

/* features */
.features{left:0;top:1680px;width:1200px;height:495px;background:var(--grey-band)}
.feature-label{font-family:"Poppins",Arial,sans-serif;font-size:13px;font-weight:500;text-align:center;width:220px}

/* testimonials */
.testimonials{left:0;top:2175px;width:1200px;height:438px;background:#fff}
.card{top:176px;width:326px;height:164px;background:#fff;box-shadow:0 4px 18px rgba(0,0,0,.10)}
.card h4{position:absolute;left:40px;top:36px;font-size:15px;font-weight:500}
.stars{position:absolute;left:40px;top:60px;color:var(--star);font-size:12px;letter-spacing:2px}
.card p{position:absolute;left:40px;top:82px;width:245px;font-size:11px;line-height:17px;color:var(--muted)}
.card .quote{position:absolute;right:22px;top:118px}
.card .tail{position:absolute;left:58px;bottom:-10px;width:18px;height:18px;background:#fff;transform:rotate(45deg);box-shadow:3px 3px 5px rgba(0,0,0,.06)}

/* footer */
.footer{left:0;top:2613px;width:1200px;height:352px;background:var(--footer);color:var(--white)}
.footer h4{position:absolute;top:75px;font-size:15px;font-weight:500}
.footer ul{list-style:none;position:absolute;left:380px;top:114px}
.footer li{font-size:12px;height:29.5px;color:#ddd}
.footer li::before{content:"›";color:#666;margin-right:12px}
.contact-row{position:absolute;left:593px;font-size:12px;color:#ddd;line-height:17px;display:flex;gap:12px}
.socials{position:absolute;left:593px;top:227px;display:flex;gap:10px}
.socials span{width:11px;height:11px;border-radius:50%;background:#fff}
.news-input{position:absolute;left:854px;top:155px;width:255px;height:41px;background:#fff;display:flex}
.news-input span{flex:1;font-size:11px;color:#999;padding:13px 0 0 40px}
.news-input b{width:41px;background:var(--blue);display:flex;align-items:center;justify-content:center}
.footer-rule{position:absolute;left:89px;top:293px;width:1022px;height:1px;background:#333}
.copyright{position:absolute;top:319px;width:1200px;text-align:center;font-size:11px;font-weight:600;color:#ddd}
.to-top{position:absolute;left:1109px;top:273px;width:40px;height:40px;border-radius:50%;background:var(--blue);display:flex;align-items:center;justify-content:center}
</style>
</head>
<body>

<header class="hero abs">
  <div class="hero-photo" role="img" aria-label="Photo of a smiling professional working on a laptop with a colleague in an office"></div>
  <div class="hero-shade"></div>
  <div class="logo abs">Logo Here</div>
  <nav class="nav abs">
    <a class="active" style="left:692px">Home</a>
    <a style="left:781px">Services</a>
    <a style="left:882px">About Us</a>
    <a style="left:988px">Contact Us</a>
    <svg width="14" height="14" viewBox="0 0 14 14"><circle cx="6" cy="6" r="4.5" fill="none" stroke="#fff" stroke-width="1.6"/><line x1="9.3" y1="9.3" x2="13" y2="13" stroke="#fff" stroke-width="1.6"/></svg>
  </nav>
  <h1 class="abs">IT Support Tailored for London City Business</h1>
  <a class="hero-link abs">View our IT Support solutions &nbsp;»</a>
</header>

<div class="scroll-btn abs">
  <svg width="104" height="104" viewBox="0 0 104 104"><path d="M46 34 L46 50 Q46 56 52 58 L52 72" fill="none" stroke="#fff" stroke-width="2"/><path d="M46 68 L52 75 L58 68" fill="none" stroke="#fff" stroke-width="2"/></svg>
</div>

<section class="about abs">
  <div class="skyline" role="img" aria-label="London skyline at dusk with Westminster Bridge and the clock tower"></div>
  <div class="eyebrow abs" style="top:161px">ABOUT US</div>
  <h2 class="section-title abs" style="top:176px">Welcome To Our Company</h2>
  <p class="about-text abs" style="top:222px">Lorem ipsum dolor sit amet, consectetuer adipiscing elit. Aenean commodo ligula eget dolor aenean massa cum sociis natoque penatibus et magnis dis parturient montes, nascetur ridiculus mus donec .</p>
  <div class="btn abs">READ MORE</div>
</section>

<section class="service support abs" role="img" aria-label="Blue-tinted photo of a support agent with a headset">
  <svg width="70" height="70" viewBox="0 0 70 70" fill="none" stroke="#fff" stroke-width="2.2"><circle cx="35" cy="28" r="12"/><path d="M19 30 V24 A16 16 0 0 1 51 24 V30"/><rect x="15" y="24" width="6" height="10" rx="2"/><rect x="49" y="24" width="6" height="10" rx="2"/><path d="M52 34 Q52 42 40 42"/><path d="M14 66 Q14 48 35 46 Q56 48 56 66 Z"/></svg>
  <h3>IT Support</h3>
  <p>Lorem ipsum dolor sit amet, consectetuer adipiscing elit aenean commodo ligula eget dolor. Aenean massa cum sociis natoque penatibus et magnis dis parturie.</p>
</section>
<section class="service security abs">
  <svg width="70" height="70" viewBox="0 0 70 70" fill="none" stroke="#111" stroke-width="2"><rect x="24" y="30" width="22" height="18" rx="2"/><path d="M28 30 V24 A7 7 0 0 1 42 24 V30"/><circle cx="35" cy="38" r="2"/><line x1="35" y1="40" x2="35" y2="44"/><path d="M24 36 H12 V20 M12 20 H6"/><circle cx="6" cy="20" r="3"/><path d="M46 36 H58 V20 H64"/><circle cx="64" cy="20" r="3"/><path d="M24 44 H12 V56 H6"/><circle cx="6" cy="56" r="3"/><path d="M46 44 H58 V56 H64"/><circle cx="64" cy="56" r="3"/><line x1="35" y1="48" x2="35" y2="62"/><circle cx="35" cy="65" r="3"/></svg>
  <h3>IT security</h3>
  <p>Lorem ipsum dolor sit amet, consectetuer adipiscing elit aenean commodo ligula eget dolor. Aenean massa cum sociis natoque penatibus et magnis dis parturie.</p>
</section>

<section class="features abs">
  <div class="eyebrow abs" style="top:112px">FEATURES</div>
  <h2 class="section-title abs" style="top:128px">Featured Solutions</h2>
  <svg class="abs" style="left:0;top:0" width="1200" height="495" viewBox="0 0 1200 495">
    <defs><linearGradient id="waveFade" x1="0" x2="1"><stop offset="0" stop-color="#1b8fd9" stop-opacity="0"/><stop offset=".12" stop-color="#1b8fd9"/><stop offset=".88" stop-color="#1b8fd9"/><stop offset="1" stop-color="#1b8fd9" stop-opacity="0"/></linearGradient></defs>
    <path d="M158 266 C230 250 260 216 314 216 C380 216 410 287 480 287 C560 287 580 218 645 218 C720 218 740 289 811 289 C880 289 900 200 1030 200" fill="none" stroke="url(#waveFade)" stroke-width="2.5"/>
    <g fill="#1b8fd9">
      <circle cx="314" cy="216" r="12"/><circle cx="480" cy="287" r="12"/><circle cx="645" cy="218" r="12"/><circle cx="811" cy="289" r="12"/>
    </g>
    <g fill="none" stroke="#1b8fd9" stroke-width="1" stroke-dasharray="2 2">
      <circle cx="314" cy="216" r="24"/><circle cx="480" cy="287" r="24"/><circle cx="645" cy="218" r="24"/><circle cx="811" cy="289" r="24"/>
    </g>
    <g fill="none" stroke="#111" stroke-width="1.8">
      <g transform="translate(296,260)"><circle cx="18" cy="18" r="6"/><circle cx="18" cy="3" r="2.5"/><circle cx="18" cy="33" r="2.5"/><circle cx="3" cy="18" r="2.5"/><circle cx="33" cy="18" r="2.5"/><circle cx="7" cy="7" r="2.5"/><circle cx="29" cy="29" r="2.5"/><circle cx="29" cy="7" r="2.5"/><circle cx="7" cy="29" r="2.5"/></g>
      <g transform="translate(460,326)"><path d="M2 6 H14 L17 10 H34 V30 H2 Z"/><circle cx="30" cy="30" r="7"/><circle cx="30" cy="30" r="2.5"/></g>
      <g transform="translate(627,258)"><rect x="4" y="4" width="28" height="19" rx="1"/><path d="M0 27 H36"/><path d="M14 18 L20 10"/></g>
      <g transform="translate(791,328)"><circle cx="20" cy="15" r="12"/><path d="M8 15 H32 M20 3 V27 M12 7 Q20 15 12 23 M28 7 Q20 15 28 23"/><rect x="4" y="28" width="32" height="6"/></g>
    </g>
  </svg>
  <div class="feature-label abs" style="left:204px;top:310px">Lumora</div>
  <div class="feature-label abs" style="left:370px;top:377px">Machine Learning</div>
  <div class="feature-label abs" style="left:535px;top:318px">Enterprises</div>
  <div class="feature-label abs" style="left:701px;top:381px">Digital Transformation</div>
</section>

<section class="testimonials abs">
  <div class="eyebrow abs" style="top:102px">TESTIMONIALS</div>
  <h2 class="section-title abs" style="top:117px">Customer Review</h2>
  <svg class="abs" style="left:1066px;top:112px" width="46" height="16" viewBox="0 0 46 16" fill="none" stroke-width="1.6"><path d="M16 8 H2 M7 3 L2 8 L7 13" stroke="#333"/><path d="M26 8 H44 M39 3 L44 8 L39 13" stroke="#1b8fd9"/></svg>

  <div class="card abs" style="left:89px"><div class="tail"></div>
    <h4>Tom Brevik</h4><div class="stars">★★★★★</div>
    <p>Lorem ipsum dolor sit amet, consectetuer adipiscing elit. Aenean commodo ligula eget dolor aenean massa.</p>
    <svg class="quote" width="20" height="16" viewBox="0 0 20 16" fill="#1b8fd9"><path d="M0 16 V8 Q0 1 8 0 V3 Q4 4 4 8 H8 V16 Z M11 16 V8 Q11 1 19 0 V3 Q15 4 15 8 H19 V16 Z"/></svg>
  </div>
  <div class="card abs" style="left:437px"><div class="tail"></div>
    <h4>Mira Tolens</h4><div class="stars">★★★★★</div>
    <p>Lorem ipsum dolor sit amet, consectetuer adipiscing elit. Aenean commodo ligula eget dolor aenean massa.</p>
    <svg class="quote" width="20" height="16" viewBox="0 0 20 16" fill="#1b8fd9"><path d="M0 16 V8 Q0 1 8 0 V3 Q4 4 4 8 H8 V16 Z M11 16 V8 Q11 1 19 0 V3 Q15 4 15 8 H19 V16 Z"/></svg>
  </div>
  <div class="card abs" style="left:787px"><div class="tail"></div>
    <h4>Dev Oranya</h4><div class="stars">★★★★★</div>
    <p>Lorem ipsum dolor sit amet, consectetuer adipiscing elit. Aenean commodo ligula eget dolor aenean massa.</p>
    <svg class="quote" width="20" height="16" viewBox="0 0 20 16" fill="#1b8fd9"><path d="M0 16 V8 Q0 1 8 0 V3 Q4 4 4 8 H8 V16 Z M11 16 V8 Q11 1 19 0 V3 Q15 4 15 8 H19 V16 Z"/></svg>
  </div>
</section>

<footer class="footer abs">
  <div class="logo abs" style="left:144px;top:137px;font-size:28px">Logo Here</div>

  <h4 style="left:380px">Quick links</h4>
  <ul><li>Home</li><li>About Us</li><li>Services</li><li>Contact Us</li></ul>

  <h4 style="left:593px">Contact Us</h4>
  <div class="contact-row" style="top:114px"><svg width="12" height="12" viewBox="0 0 12 12" fill="#1b8fd9"><path d="M2 0 L5 3 L3.5 5 Q5 8 7 8.5 L9 7 L12 10 L10 12 Q3 11 0 2 Z"/></svg><span>Call : +1 (555) 010-4477</span></div>
  <div class="contact-row" style="top:145px"><svg width="12" height="14" viewBox="0 0 12 14" fill="#1b8fd9"><path d="M6 0 A5 5 0 0 1 11 5 Q11 8 6 14 Q1 8 1 5 A5 5 0 0 1 6 0 Z"/><circle cx="6" cy="5" r="2" fill="#000"/></svg><span>00000 Sample des Vallerins<br>Suite 000</span></div>
  <div class="contact-row" style="top:192px"><svg width="12" height="10" viewBox="0 0 12 10" fill="#1b8fd9"><rect width="12" height="10"/><path d="M0 0 L6 5 L12 0" stroke="#000" fill="none"/></svg><span>Email : hello@mailrun.com</span></div>
  <div class="socials"><span></span><span></span><span></span><span></span></div>

  <h4 style="left:854px">Newsletter</h4>
  <div class="abs" style="left:852px;top:112px;font-size:12px;color:#ddd">Enter your email adrress for getting updates</div>
  <div class="news-input"><span>Enter your email.</span><b><svg width="14" height="14" viewBox="0 0 14 14" fill="#fff"><path d="M0 6 L14 0 L10 14 L7 8 Z"/></svg></b></div>

  <div class="footer-rule"></div>
  <div class="copyright">© COPYRIGHT 2018 &nbsp;| ALL RIGHT RESERVED</div>
  <div class="to-top"><svg width="10" height="6" viewBox="0 0 10 6" fill="none" stroke="#fff" stroke-width="1.6"><path d="M1 5 L5 1 L9 5"/></svg></div>
</footer>

</body>
</html>
```